4th Generation Family Business Needs a New Card Design!

We are a family owned 4th Generation company. We are based in the Sydney, Australia area and we are desperately in need of a more modern and classy card. We are monumental masons who design, supply & erect lasting memorials throughout cemeteries in Sydney. Our customers are normally in a period of grieving. I have attached logo files that will need to be implemented on the card. Company was established 1935. Australian Owned and Operated. Card needs to be designed to PRINTLY.com specification.

Target Market(s)

Our target market is based upon people that a grieving for family members that have passed away. We also deal with alot of companies that own and operate cemeteries.

Industry/Entity Type

Business

Contact Information for Business Card

Oliver Brantley, Operations Manager, 0417552908, oliver@hollowaystoneworks.com.au
Martin Brantley, Director, 0431906627, martin@hollowaystoneworks.com.au
Phone # 02 9634 2258
Website: www.hollowaystoneworks.com.au
Address: Suite 17, 8 Calloway Lane, East Penrose, Sydney NSW 2290

Font styles to use
Serif
Decorative
Script

Requirements
Must have
• Would like to see the logo nicely implemented with a modern design. Embossed lettering would be a nice additive.

```html
<!DOCTYPE html>
<html lang="en">
<head>
<meta charset="utf-8">
<title>Holloway Stoneworks – Business Card</title>
<link href="https://fonts.googleapis.com/css2?family=Arimo:wght@400;700&display=swap" rel="stylesheet">
<style>
  :root {
    --page: #ece9e4;
    --card: #f8f8f6;
    --ink: #2f2f31;
    --ink-soft: #4a4a4d;
    --gold: #f0d335;
    --shadow: rgba(40, 30, 20, 0.22);
  }
  html, body {
    margin: 0;
    padding: 0;
    width: 1200px;
    height: 902px;
    overflow: hidden;
    background: var(--page);
    font-family: "Arimo", Arial, sans-serif;
    color: var(--ink);
  }
  .canvas {
    position: relative;
    width: 1200px;
    height: 902px;
  }
  .card {
    position: absolute;
    width: 560px;
    height: 320px;
    background: var(--card);
    box-shadow: 0 3px 0 #e2e2df, 0 6px 0 #d8d8d4, 0 14px 30px var(--shadow);
    overflow: hidden;
  }
  .card--front { left: 110px; top: 90px; }
  .card--back  { left: 530px; top: 480px; }

  .wordmark {
    position: absolute;
    display: flex;
    align-items: center;
    gap: 12px;
    font-weight: 700;
    text-transform: uppercase;
    letter-spacing: 0.12em;
    color: var(--ink);
    white-space: nowrap;
  }
  .wordmark__square {
    width: 14px;
    height: 14px;
    background: var(--gold);
    flex: none;
  }
  .wordmark__text { display: block; line-height: 1.2; }
  .card--front .wordmark {
    left: 0; right: 0;
    top: 145px;
    justify-content: center;
    font-size: 24px;
  }
  .card--back .wordmark {
    left: 40px;
    top: 138px;
    font-size: 18px;
  }
  .card--back .wordmark__line { display: block; }

  .swoosh {
    position: absolute;
    left: 0; top: 0;
    width: 560px; height: 320px;
  }

  .contact {
    position: absolute;
    right: 34px;
    top: 34px;
    text-align: right;
    font-size: 11px;
    line-height: 1.35;
    color: var(--ink);
  }
  .contact__people {
    display: flex;
    justify-content: flex-end;
    gap: 8px;
    text-align: left;
    margin-bottom: 26px;
  }
  .person__name { font-size: 15px; line-height: 1.1; }
  .person__role { font-size: 11px; color: var(--ink-soft); }
  .person + .person {
    border-left: 2px solid var(--ink);
    padding-left: 8px;
  }
  .contact__block { margin-bottom: 14px; }
</style>
</head>
<body>
<main class="canvas">

  <section class="card card--front" aria-label="Card front">
    <div class="wordmark"><span class="wordmark__square"></span><span class="wordmark__text">Holloway Stoneworks</span></div>
  </section>

  <section class="card card--back" aria-label="Card back">
    <svg class="swoosh" viewBox="0 0 560 320" aria-hidden="true">
      <path d="M214 0 C 300 60, 330 170, 300 320 L 280 320 C 306 180, 280 70, 196 0 Z" fill="var(--gold)"/>
    </svg>

    <div class="wordmark">
      <span class="wordmark__square"></span>
      <span class="wordmark__text"><span class="wordmark__line">Holloway</span><span class="wordmark__line">Stoneworks</span></span>
    </div>

    <div class="contact">
      <div class="contact__people">
        <div class="person">
          <div class="person__name">Oliver Brantley</div>
          <div class="person__role">Operations Manager</div>
        </div>
        <div class="person">
          <div class="person__name">Martin Brantley</div>
          <div class="person__role">Director</div>
        </div>
      </div>
      <div class="contact__block">0417552908 / 0431906627</div>
      <div class="contact__block">
        oliver@hollowaystoneworks.com.au<br>
        martin@hollowaystoneworks.com.au
      </div>
      <div class="contact__block">www.hollowaystoneworks.com.au</div>
      <div class="contact__block">
        Suite 17, 8 Calloway Lane, East Penrose,<br>
        Sydney NSW 2290
      </div>
    </div>
  </section>

</main>
</body>
</html>
```